Kestrel Fitness Studio Retail Tube Design

We require a design for cardboard tubes, like images included, which will be the main packaging for the clothing sold in our fitness studio. Kestrel Fitness Studio is an upscale customer service driven fitness studio that is geared towards improving our clients/members quality of life by marrying cutting edge technology like 3D scanning and metabolic measurement with first class training based on 30+ years of experience in the industry.

The project will require a design which revolves around the tube seamlessly including the lid and its top and must include the company logo, which is included, along with our web address (www.kestrelgymhall.example).

The final design should be a bold, sleek design which stands out so when people see the tube they will either know it’s from our studio or be curious as to want company it’s from. Similar to the impact the Moravanti bag has that is given to all their customers.

Target Market(s)

Individuals and groups seeking individualize fitness programs which produce results.

Industry/Entity Type

Clothing

Colors

Designer to choose colors to be used in the design.

Requirements
Must have
• Logo and website address

```html
<!DOCTYPE html>
<html lang="en">
<head>
<meta charset="utf-8">
<title>Kestrel Fitness Studio – Retail Tube Wraps</title>
<link href="https://fonts.googleapis.com/css2?family=Raleway:wght@300&family=Oswald:wght@600&family=Roboto:wght@400&display=swap" rel="stylesheet">
<style>
  :root {
    --page-bg: #e9e9ea;
    --wrap-black: #1c1c1d;
    --band-navy: #0d0d16;
    --brand-red: #e0283a;
    --logo-grey: #c9c9c9;
    --ring-white: #f4f4f4;
    --photo-top: #a9b04a;
    --photo-mid: #b14a48;
    --photo-low: #6d3f7a;
    --photo-edge: #1e1a24;
  }
  * { box-sizing: border-box; margin: 0; padding: 0; }
  html, body { width: 1111px; height: 1200px; overflow: hidden; background: var(--page-bg); }
  .sheet {
    position: relative; width: 1111px; height: 1200px;
    display: flex; justify-content: center; align-items: center; gap: 70px;
  }
  .tube-wrap {
    position: relative; width: 470px; height: 1130px;
    background: var(--wrap-black); overflow: hidden;
    display: flex; flex-direction: column;
  }
  .brand-band {
    height: 320px; display: flex; flex-direction: column;
    align-items: center; justify-content: flex-end; padding-bottom: 34px;
  }
  .brand-name {
    font-family: "Raleway", sans-serif; font-weight: 300;
    color: var(--logo-grey); text-align: center; line-height: 1;
  }
  .brand-name .word { display: block; font-size: 66px; letter-spacing: 2px; }
  .brand-name .sub { display: block; font-size: 17px; letter-spacing: 4px; margin-top: 12px; }
  .hero-photo {
    flex: 1;
    background:
      radial-gradient(ellipse 70% 60% at 50% 50%, transparent 40%, rgba(20,16,26,0.55) 100%),
      linear-gradient(180deg, var(--photo-top) 0%, #8f7a45 25%, var(--photo-mid) 55%, var(--photo-low) 80%, var(--photo-edge) 100%);
  }
  .feature-band {
    height: 160px; background: var(--band-navy); position: relative;
    display: flex; flex-direction: column; align-items: center;
  }
  .feature-line {
    position: absolute; left: 0; right: 0; top: 32px; height: 3px; background: var(--ring-white);
  }
  .feature-badges {
    position: relative; display: flex; gap: 34px; margin-top: -12px;
  }
  .badge {
    width: 84px; height: 84px; border-radius: 50%;
    background: var(--brand-red); border: 5px solid var(--ring-white);
    box-shadow: inset 0 0 0 3px #a81a28;
    display: flex; align-items: center; justify-content: center;
    font-family: "Oswald", sans-serif; font-weight: 600;
    color: #fff; font-size: 19px; letter-spacing: 0.3px;
  }
  .badge.wide { font-size: 18px; }
  .feature-copy {
    font-family: "Roboto", sans-serif; font-size: 10.5px; line-height: 1.35;
    color: var(--brand-red); text-align: center; width: 380px; margin-top: 12px;
  }
  .web-address {
    font-family: "Roboto", sans-serif; font-size: 19px; letter-spacing: 0.5px;
    color: var(--brand-red); margin-top: 10px;
  }
</style>
</head>
<body>
<main class="sheet">
  <section class="tube-wrap tube-wrap--men">
    <header class="brand-band">
      <div class="brand-name"><span class="word">kestrel</span><span class="sub">FITNESS STUDIO</span></div>
    </header>
    <div class="hero-photo" role="img" aria-label="Photo of a man lifting his shirt to show toned abdominal muscles, colour-graded from yellow-green to red and purple"></div>
    <footer class="feature-band">
      <div class="feature-line"></div>
      <div class="feature-badges">
        <div class="badge">COMFY</div>
        <div class="badge wide">TRANDY</div>
        <div class="badge">SOFT</div>
      </div>
      <p class="feature-copy">Lorem ipsum dolor sit amet, consectetur adipiscing elit. Phasellus agittis nulla id pretium luctus. Curabitur ullamcorper vehicula cursus.</p>
      <p class="web-address">www.kestrelgymhall.example</p>
    </footer>
  </section>

  <section class="tube-wrap tube-wrap--women">
    <header class="brand-band">
      <div class="brand-name"><span class="word">kestrel</span><span class="sub">FITNESS STUDIO</span></div>
    </header>
    <div class="hero-photo" role="img" aria-label="Photo of a woman lifting her top to show toned abdominal muscles, colour-graded from yellow-green to red and purple"></div>
    <footer class="feature-band">
      <div class="feature-line"></div>
      <div class="feature-badges">
        <div class="badge">COMFY</div>
        <div class="badge wide">TRANDY</div>
        <div class="badge">SOFT</div>
      </div>
      <p class="feature-copy">Lorem ipsum dolor sit amet, consectetur adipiscing elit. Phasellus agittis nulla id pretium luctus. Curabitur ullamcorper vehicula cursus.</p>
      <p class="web-address">www.kestrelgymhall.example</p>
    </footer>
  </section>
</main>
</body>
</html>
```